Two-page Website Design for Construction Business

Make a one or two-page website. (Two-page if it is better to put "contact us" on separate page.
Must be cell phone responsive.
Needs to be posted to velbrino.com.
Some minor graphic design is required.
Sample layout is provided in ppt file.
All content is provided in ppt file except the graphics need to be professionally made.
Updates
Reason: Only 3 designers competing for this simple site. I will extend for 5 days.
Suggested photos from framquilla:
Storefront: 144849883
Industrial: 139927951
ADA: 282622679
Ballistic: 311146781 or 652211317
Corrosion: 465155321
Clean room: 478585840
Hurricane: 110081945 or 127898684
Fire: 271704542
Chemical: 242308249 or 93390571
Target Market(s)
Construction
Industry/Entity Type
Construction
Coding
Coded - Design and coding required
Number of Pages Required
2 page
Colors
Designer to choose colors to be used in the design.
Requirements
Must have
- I'm not sure what "uncoded" means, but the site must be loaded to velbrino.com and it must be operational.
- Please use standard error checking such as only numbers for phone info, correctly formatted email addresses, etc.
- I must be able to update the site easily -- wordpress.

```html
<!DOCTYPE html>
<html lang="en">
<head>
<meta charset="utf-8">
<title>Gulfline DoorWorks – Commercial Door Installation &amp; Repair</title>
<link href="https://fonts.googleapis.com/css2?family=Lato:wght@400;700;900&family=Titan+One&family=Roboto+Slab:wght@400;500&display=swap" rel="stylesheet">
<style>
:root{
  --blue:#2b3990;
  --blue-band:#3444a6;
  --blue-deep:#1a2d9c;
  --red:#ed1c24;
  --white:#ffffff;
  --grey:#eeeeee;
  --field:#f2f2f2;
  --ink:#222222;
  --muted:#9a9a9a;
}
*{box-sizing:border-box;margin:0;padding:0}
html,body{width:1200px;height:2466px;overflow:hidden;background:var(--white)}
body{position:relative;font-family:"Lato",sans-serif;color:var(--ink)}
.abs{position:absolute}

/* header */
.site-header{left:0;top:0;width:1200px;height:102px;background:var(--white);box-shadow:0 2px 6px rgba(0,0,0,.15);z-index:5}
.brand{left:79px;top:26px;display:flex;align-items:center;gap:12px}
.brand-mark{width:44px;height:44px;background:var(--blue)}
.brand-name{font-family:"Lato",sans-serif;font-weight:900;font-size:30px;color:var(--blue)}
.main-nav{left:480px;top:45px;width:572px;display:flex;justify-content:space-between;font-size:13px;color:var(--muted)}
.main-nav .current{color:var(--blue)}
.nav-divider{left:1075px;top:34px;width:2px;height:34px;background:var(--blue)}
.search-icon{left:1090px;top:42px}

/* hero */
.hero{left:0;top:102px;width:1200px;height:621px;overflow:hidden}
.hero-photo{left:0;top:0;width:1200px;height:621px;background:radial-gradient(ellipse at 35% 45%,#3a3430 0%,#2a3a9a 22%,#1b36b8 50%,#0d1f7a 100%)}
.hero-skyline{left:661px;top:103px;width:411px;height:146px;border:6px solid var(--white);background:linear-gradient(180deg,#a9c9e8,#4a78b0);display:flex}
.hero-skyline i{flex:1;border-right:4px solid var(--white)}
.hero-skyline i:last-child{border-right:0}
.hero-floor{left:0;top:540px}
.hero-title{right:79px;top:403px;text-align:right;font-family:"Titan One",sans-serif;font-weight:400;font-size:39px;line-height:48px;color:var(--white);letter-spacing:1px;text-shadow:0 2px 3px rgba(0,0,0,.35)}
.hero-sub{right:79px;top:410px;width:520px;text-align:right;font-size:18px;line-height:23px;color:#e6ebff}
.hero-area{right:79px;top:474px;text-align:right;font-size:22px;font-weight:700;color:var(--white)}

/* contact cards */
.card{width:313px;height:232px;top:735px;background:var(--red);color:var(--white);text-align:center}
.card-phone{left:77px}
.card-mail{left:810px}
.card-badge{width:112px;height:112px;border-radius:50%;background:var(--blue-deep);border:7px solid #d8d8d8;top:682px;display:flex;align-items:center;justify-content:center}
.card-lines{position:absolute;left:0;width:100%;top:74px;font-size:25px;font-weight:700;line-height:33px}
.card-mail .card-lines{font-size:21px;top:78px}
.card-btn{position:absolute;top:161px;left:53px;width:207px;height:51px;background:var(--blue);color:var(--white);font-size:18px;font-weight:700;display:flex;align-items:center;justify-content:center}

/* quote form */
.quote{left:424px;top:677px;width:354px;height:438px;background:var(--white);border-radius:6px;box-shadow:0 4px 18px rgba(0,0,0,.18);z-index:3}
.quote h2{position:absolute;top:30px;width:100%;text-align:center;font-family:"Roboto Slab",serif;font-weight:500;font-size:29px;color:var(--red)}
.quote .field{position:absolute;left:31px;width:290px;background:var(--field);font-size:13px;color:#555;padding:13px 21px}
.quote .submit{position:absolute;left:72px;top:342px;width:208px;height:50px;background:var(--blue);color:var(--white);font-weight:700;font-size:18px;display:flex;align-items:center;justify-content:center}

/* about */
.about{left:0;top:1018px;width:1200px;height:347px;background:var(--blue-band)}
.about h2{position:absolute;top:130px;width:100%;text-align:center;font-family:"Roboto Slab",serif;font-weight:400;font-size:50px;line-height:60px}
.about h2 .lead{color:var(--red)}
.about h2 .name{color:var(--white)}
.about p{position:absolute;left:123px;top:214px;width:967px;text-align:center;font-size:13px;line-height:21px;color:#aab3e6}
.spec{width:117px;top:1324px;text-align:center}
.spec-dot{width:82px;height:82px;margin:0 auto;border-radius:50%;background:var(--white);border:3px solid #c8c8c8;display:flex;align-items:center;justify-content:center}
.spec-dot span{width:64px;height:64px;border-radius:50%;background:var(--blue);display:flex;align-items:center;justify-content:center}
.spec-label{margin-top:12px;font-size:18px;color:#333}
.spec-label.active{color:var(--red)}

/* center brand */
.mid-brand{left:0;top:1515px;width:1200px;display:flex;justify-content:center;align-items:center;gap:16px}
.mid-brand .brand-mark{width:56px;height:56px}
.mid-brand .brand-name{font-size:40px}

/* tiles */
.tile{top:1621px;width:400px;height:312px;background:var(--grey);text-align:center}
.tile-services{background:var(--red);color:var(--white)}
.tile h3{position:absolute;top:150px;width:100%;font-weight:400;font-size:22px;letter-spacing:1px}
.tile .tile-icon{position:absolute;top:50px;left:0;width:100%;display:flex;justify-content:center}
.tile-btn{position:absolute;top:201px;width:188px;height:50px;background:var(--blue);color:var(--white);font-size:18px;display:flex;align-items:center;justify-content:center}
.tile-services .tile-btn{background:var(--white);color:var(--red)}

/* contact */
.contact{left:0;top:1933px;width:1200px;height:470px;background:linear-gradient(180deg,rgba(58,78,180,.97),rgba(40,60,160,.92)),linear-gradient(90deg,#6b5a55,#8a8f99)}
.contact h2{position:absolute;top:50px;width:100%;text-align:center;font-family:"Roboto Slab",serif;font-weight:400;font-size:46px}
.contact h2 .lead{color:var(--red)}
.contact h2 .rest{color:var(--white)}
.inquiry-title{left:79px;top:134px;color:var(--white);font-size:18px;font-weight:700;letter-spacing:.5px}
.inquiry-title span{font-weight:400}
.input{background:var(--field);font-size:11px;color:#999;padding:13px 14px;height:41px}
.msg{left:77px;top:231px;width:697px;height:144px}
.send{left:641px;top:335px;width:80px;height:80px;border-radius:50%;background:var(--blue);border:5px solid #d8d8d8;display:flex;align-items:center;justify-content:center}
.info{left:857px;top:125px;width:200px;text-align:center;color:var(--white)}
.info h4{font-size:19px;font-weight:700;letter-spacing:1px;margin-bottom:20px}
.info p{font-size:14px;line-height:21px}
.info svg{display:block;margin:0 auto 4px}
.info .group{margin-bottom:12px}

/* footer */
.site-footer{left:0;top:2403px;width:1200px;height:63px;background:var(--red);color:var(--white)}
.copy{left:79px;top:23px;font-size:14px}
.copy b{font-size:17px}
.copy .sep{margin:0 12px}
.social{right:83px;top:10px;display:flex;gap:10px}
.social span{width:42px;height:42px;border-radius:50%;border:2px solid var(--white);display:flex;align-items:center;justify-content:center}
</style>
</head>
<body>

<header class="site-header abs">
  <div class="brand abs"><span class="brand-mark"></span><span class="brand-name">Gulfline DoorWorks</span></div>
  <nav class="main-nav abs">
    <span class="current">Home</span><span>Speciality</span><span>Services</span><span>Why us</span><span>Terms</span><span>Quote or service</span><span>Contact</span>
  </nav>
  <div class="nav-divider abs"></div>
  <svg class="search-icon abs" width="18" height="18" viewBox="0 0 18 18"><circle cx="7" cy="7" r="5" fill="none" stroke="#ed1c24" stroke-width="2.5"/><line x1="11" y1="11" x2="16" y2="16" stroke="#ed1c24" stroke-width="2.5"/></svg>
</header>

<section class="hero abs">
  <div class="hero-photo abs" role="img" aria-label="Modern dark wood commercial door and a potted plant against a bright blue wall"></div>
  <div class="hero-skyline abs" role="img" aria-label="Three photos of a city skyline"><i></i><i></i><i></i></div>
  <svg class="hero-floor abs" width="1200" height="81" viewBox="0 0 1200 81" preserveAspectRatio="none"><path d="M0 60 Q600 -20 1200 40 L1200 81 L0 81 Z" fill="#ffffff"/></svg>
  <h1 class="hero-title abs" style="top:300px">COMMERCIAL DOOR<br>INSTALLATION &amp; REPAIR</h1>
  <p class="hero-sub abs">Your First and Only Call!! If we don't provide it, install it, or repair it, we'll recommend a great company that will</p>
  <p class="hero-area abs">Proudly serving Houston and the surrounding areas</p>
</section>

<div class="card card-phone abs">
  <div class="card-lines">Wade : 555-410-2287<br>Colton : 555-410-3395</div>
  <div class="card-btn">Same Day Responce</div>
</div>
<div class="card-badge abs" style="left:177px">
  <svg width="50" height="50" viewBox="0 0 50 50"><circle cx="25" cy="25" r="22" fill="none" stroke="#fff" stroke-width="2.5"/><path d="M17 13c3-2 5 1 6 4 1 2-2 3-1 5 1 3 4 6 7 7 2 1 3-2 5-1 3 1 6 3 4 6-2 3-6 3-9 1-6-3-11-8-14-14-1-3-1-6 2-8z" fill="#fff"/></svg>
</div>

<div class="card card-mail abs">
  <div class="card-lines">Email :<br>info@gulflinedoorworks.com</div>
  <div class="card-btn">Next Day Responce</div>
</div>
<div class="card-badge abs" style="left:910px">
  <svg width="54" height="40" viewBox="0 0 54 40"><rect x="2" y="2" width="50" height="36" fill="none" stroke="#fff" stroke-width="3"/><path d="M2 2 L27 22 L52 2 M2 38 L20 17 M52 38 L34 17" fill="none" stroke="#fff" stroke-width="3"/></svg>
</div>

<form class="quote abs">
  <h2>NEED A QUOTE?</h2>
  <div class="field" style="top:86px;height:43px">Name:</div>
  <div class="field" style="top:132px;height:43px">Mobile Phone:</div>
  <div class="field" style="top:180px;height:42px">Email:</div>
  <div class="field" style="top:227px;height:110px">Message:</div>
  <div class="submit">Submit</div>
</form>

<section class="about abs">
  <h2><span class="lead">About</span> <span class="name">Gulfline DoorWorks</span></h2>
  <p>Lorem Ipsum is simply dummy text of the printing and typesetting industry. Lorem Ipsum has been the industry's standard dummy text ever since the 1500s, when an unknown printer took a galley of type and scrambled it to make a type specimen book. It has survived not only five centuries, but also the leap into electronic typesetting, remaining essentially unchanged.</p>
</section>

<div class="spec abs" style="left:75px"><div class="spec-dot"><span><svg width="34" height="30" viewBox="0 0 34 30"><rect x="2" y="2" width="30" height="8" fill="#fff"/><rect x="4" y="12" width="26" height="16" fill="none" stroke="#fff" stroke-width="2.5"/><rect x="13" y="16" width="8" height="12" fill="#fff"/></svg></span></div><div class="spec-label active">Storefront</div></div>
<div class="spec abs" style="left:192px"><div class="spec-dot"><span><svg width="34" height="30" viewBox="0 0 34 30"><path d="M2 28 V12 L10 17 V12 L18 17 V12 L26 17 V2 H31 V28 Z" fill="#fff"/></svg></span></div><div class="spec-label">Industrial</div></div>
<div class="spec abs" style="left:309px"><div class="spec-dot"><span><svg width="30" height="32" viewBox="0 0 30 32"><circle cx="13" cy="4" r="3.5" fill="#fff"/><path d="M12 9 V18 H22 L26 28" fill="none" stroke="#fff" stroke-width="3"/><circle cx="12" cy="22" r="8" fill="none" stroke="#fff" stroke-width="2.5"/></svg></span></div><div class="spec-label">ADA</div></div>
<div class="spec abs" style="left:425px"><div class="spec-dot"><span><svg width="30" height="32" viewBox="0 0 30 32"><circle cx="15" cy="5" r="4" fill="#fff"/><rect x="10" y="10" width="10" height="14" rx="3" fill="#fff"/><rect x="10" y="24" width="3" height="7" fill="#fff"/><rect x="17" y="24" width="3" height="7" fill="#fff"/></svg></span></div><div class="spec-label">Cleanroom</div></div>
<div class="spec abs" style="left:542px"><div class="spec-dot"><span><svg width="32" height="32" viewBox="0 0 32 32"><path d="M4 6 L24 22 L20 26 L8 14 Z" fill="none" stroke="#fff" stroke-width="2.5"/><path d="M20 26 L26 30" stroke="#fff" stroke-width="3"/></svg></span></div><div class="spec-label">Ballistic</div></div>
<div class="spec abs" style="left:659px"><div class="spec-dot"><span><svg width="32" height="32" viewBox="0 0 32 32"><path d="M4 6 H28 M7 12 H25 M10 18 H22 M13 24 H19 M15 29 H17" stroke="#fff" stroke-width="3" stroke-linecap="round"/></svg></span></div><div class="spec-label">Hurricane</div></div>
<div class="spec abs" style="left:776px"><div class="spec-dot"><span><svg width="30" height="32" viewBox="0 0 30 32"><path d="M11 2 H19 M12 2 V12 L3 28 H27 L18 12 V2" fill="none" stroke="#fff" stroke-width="2.5"/><path d="M7 22 H23 L26 28 H4 Z" fill="#fff"/></svg></span></div><div class="spec-label">Chemical</div></div>
<div class="spec abs" style="left:892px"><div class="spec-dot"><span><svg width="28" height="32" viewBox="0 0 28 32"><path d="M14 2 C18 10 24 13 24 21 A10 10 0 0 1 4 21 C4 15 8 13 9 8 C11 12 12 14 14 15 C15 10 14 6 14 2 Z" fill="#fff"/></svg></span></div><div class="spec-label">Fire</div></div>
<div class="spec abs" style="left:1009px"><div class="spec-dot"><span><svg width="32" height="32" viewBox="0 0 32 32"><circle cx="16" cy="16" r="12" fill="none" stroke="#fff" stroke-width="2.5"/><circle cx="12" cy="13" r="3" fill="#fff"/><circle cx="20" cy="19" r="2.5" fill="#fff"/></svg></span></div><div class="spec-label">Corrosion</div></div>

<div class="mid-brand abs"><span class="brand-mark"></span><span class="brand-name">Gulfline DoorWorks</span></div>

<div class="tile abs" style="left:0">
  <div class="tile-icon"><svg width="70" height="80" viewBox="0 0 70 80"><path d="M10 38 H24 V76 H10 Z M28 40 L40 8 C46 6 48 12 46 18 L42 32 H62 C68 32 68 40 64 42 C68 44 66 50 62 51 C65 54 62 58 58 59 C60 63 56 68 52 68 H28 Z" fill="none" stroke="#555" stroke-width="4" stroke-linejoin="round"/></svg></div>
  <h3>SPECIALITIES</h3>
  <div class="tile-btn" style="left:110px">Click to see</div>
</div>
<div class="tile tile-services abs" style="left:400px">
  <div class="tile-icon"><svg width="96" height="80" viewBox="0 0 96 80"><g fill="#fff"><circle cx="34" cy="42" r="18"/><circle cx="68" cy="22" r="12"/><circle cx="68" cy="62" r="12"/></g><g stroke="#fff" stroke-width="7"><line x1="34" y1="18" x2="34" y2="66"/><line x1="10" y1="42" x2="58" y2="42"/><line x1="17" y1="25" x2="51" y2="59"/><line x1="51" y1="25" x2="17" y2="59"/><line x1="68" y1="6" x2="68" y2="38"/><line x1="52" y1="22" x2="84" y2="22"/><line x1="68" y1="46" x2="68" y2="78"/><line x1="52" y1="62" x2="84" y2="62"/></g><g fill="#ed1c24"><circle cx="34" cy="42" r="7"/><circle cx="68" cy="22" r="5"/><circle cx="68" cy="62" r="5"/></g></svg></div>
  <h3>SERVICES</h3>
  <div class="tile-btn" style="left:106px">Click to see</div>
</div>
<div class="tile abs" style="left:800px">
  <div class="tile-icon"><svg width="80" height="80" viewBox="0 0 80 80"><circle cx="40" cy="40" r="34" fill="#d9d9d9" stroke="#666" stroke-width="5"/><path d="M28 30 C28 18 52 16 52 30 C52 40 40 40 40 50" fill="none" stroke="#555" stroke-width="7" stroke-linecap="round"/><circle cx="40" cy="62" r="5" fill="#555"/></svg></div>
  <h3>WHY US</h3>
  <div class="tile-btn" style="left:122px">Click to see</div>
</div>

<section class="contact abs" role="img" aria-label="Company service van parked outside a brick building, tinted blue">
  <h2><span class="lead">Contact</span> <span class="rest">Us</span></h2>
  <div class="inquiry-title abs">INQUIRY FORM – <span>Request a Quote or Send Us a Message</span></div>
  <div class="input abs" style="left:77px;top:168px;width:219px">Name</div>
  <div class="input abs" style="left:317px;top:168px;width:217px">E-Mail</div>
  <div class="input abs" style="left:556px;top:168px;width:218px">Subject</div>
  <div class="input msg abs">Message</div>
  <div class="send abs"><svg width="32" height="24" viewBox="0 0 32 24"><rect x="1.5" y="1.5" width="29" height="21" fill="none" stroke="#fff" stroke-width="2.5"/><path d="M1.5 1.5 L16 13 L30.5 1.5" fill="none" stroke="#fff" stroke-width="2.5"/></svg></div>
  <div class="info abs">
    <h4>CONTACT INFO</h4>
    <div class="group"><svg width="26" height="34" viewBox="0 0 26 34"><path d="M13 32 C5 20 2 16 2 12 A11 11 0 0 1 24 12 C24 16 21 20 13 32 Z" fill="none" stroke="#fff" stroke-width="2"/><circle cx="13" cy="12" r="4" fill="none" stroke="#fff" stroke-width="2"/></svg><p>P.O. Box 4470<br>Bayfield,TX 20915</p></div>
    <div class="group"><svg width="30" height="30" viewBox="0 0 30 30"><path d="M7 3c3-1 4 3 5 5 0 2-2 3-1 4 1 3 4 6 7 7 1 1 2-1 4-1 2 1 6 2 5 5-1 3-4 4-8 2C12 22 7 17 4 11 2 7 4 4 7 3z" fill="none" stroke="#fff" stroke-width="2"/></svg><p>Wade : 555-410-2287<br>Colton : 555-410-3395</p></div>
    <div class="group"><svg width="32" height="22" viewBox="0 0 32 22"><rect x="1" y="1" width="30" height="20" fill="none" stroke="#fff" stroke-width="2"/><path d="M1 1 L16 12 L31 1 M1 21 L12 10 M31 21 L20 10" fill="none" stroke="#fff" stroke-width="2"/></svg><p>info@gulflinedoorworks.com</p></div>
  </div>
</section>

<footer class="site-footer abs">
  <div class="copy abs">© <b>Gulfline DoorWorks</b> - 2017. All Rights Reserved. SITEMAP<span class="sep">|</span><b style="font-size:14px">TERMS &amp; CONDITIONS</b></div>
  <div class="social abs">
    <span></span><span></span><span></span><span></span>
    <span><svg width="18" height="13" viewBox="0 0 18 13"><rect x="1" y="1" width="16" height="11" fill="none" stroke="#fff" stroke-width="1.8"/><path d="M1 1 L9 7 L17 1" fill="none" stroke="#fff" stroke-width="1.8"/></svg></span>
  </div>
</footer>

</body>
</html>
```